Mind blowing and web Design Needed For Online Retailer that sells everything from electronics etc

We are a company that will be selling everything from books to electronics in the same mold as brindlecart.com
We need a clean sleek design in the quince mold. I want the website to be uncluttered but dynamic and inviting.
Dont want it too busy, so that won't scare the buyers to the site.
Please go to sofadeals.com to see the website in its present incarnation. I would like to keep the present colours if possible, but if there is a better colour combination that will convey our message then feel free to go with that.
If you willl notice, our current logo is a figure reclining in a chair while everything it wants comes to it.
Our slogan is "Lazy is good!"
We would also like to have banners on the site with someone smiling to themselves with a caption saying "I was lazy today and got 20% off my laptop"
Our main competitor is momtelo.com so we need our site to make a bigger impact
Internet savvy young people 16-50
Electronics

```html
<!DOCTYPE html>
<html lang="en">
<head>
<meta charset="utf-8">
<title>Sofadeals – Lazy is good!</title>
<link href="https://fonts.googleapis.com/css2?family=Open+Sans:wght@400;600;700&family=Oswald:wght@400;500&family=Noto+Serif:ital,wght@0,400;1,400&family=Lobster+Two&display=swap" rel="stylesheet">
<style>
:root{
  --topbar:#1b1b1b;
  --ink:#333;
  --muted:#555;
  --orange:#f5a623;
  --orange-dark:#e08a0c;
  --nav-active:#3a3a3a;
  --red:#e01b1b;
  --green:#5c9a1c;
  --blue:#2a86c9;
  --line:#d9d9d9;
  --card1-bg:#f3efeb;--card1-ink:#5a4a44;--card1-tag:#9a6b78;
  --card2-bg:#e7f3ee;--card2-ink:#3f8a6a;--card2-tag:#3f6c5a;
  --card3-bg:#fdf0e5;--card3-ink:#d4560f;--card3-tag:#7a5445;
  --footer:#1d2f47;
  --footer-line:#2c4260;
  --gold:#e5b437;
}
*{box-sizing:border-box;margin:0;padding:0}
html,body{width:855px;height:1200px;overflow:hidden;background:#fff}
body{position:relative;font-family:"Open Sans",Arial,sans-serif;color:var(--ink)}
.abs{position:absolute}

/* top bar */
.topbar{left:0;top:0;width:855px;height:18px;background:var(--topbar)}
.toplinks{left:101px;top:3px;font-size:8.5px;color:#fff;display:flex;gap:6px}
.toplinks span.sep{color:#aaa}
.top-phone{left:594px;top:2px;display:flex;align-items:center;gap:5px;color:#fff;font-size:10px;font-weight:700}
.live-help{left:689px;top:2px;display:flex;align-items:center;gap:5px;color:#fff;font-size:9.5px;font-weight:700}

/* header */
.brand{left:101px;top:26px;width:62px}
.brand-square{width:38px;height:38px;background:#e8d94a;margin:4px 0 6px 10px}
.brand-name{font-family:"Noto Serif",Georgia,serif;font-size:10px;color:#222}
.promo{left:373px;top:23px;font-family:"Noto Serif",Georgia,serif;font-size:11px;color:#333}
.promo em{color:var(--red)}
.search{left:207px;top:45px;width:367px;height:41px;background:#e4e4e4;border-radius:3px}
.search-cat{left:8px;top:9px;width:80px;height:23px;background:#fff;border:1px solid #ccc;font-size:8px;color:#888;padding:6px 5px}
.search-cat::after{content:"▾";position:absolute;right:6px;top:5px;color:#999}
.search-input{left:95px;top:9px;width:231px;height:23px;background:#fff;border:1px solid #ccc;font-size:8px;color:#888;padding:6px 7px}
.search-btn{left:332px;top:9px;width:28px;height:23px;background:var(--blue);border-radius:3px;display:flex;align-items:center;justify-content:center}
.slogan{left:633px;top:22px;font-family:"Lobster Two",cursive;font-size:21px;color:var(--green)}
.bag{left:605px;top:48px}
.bag-title{left:641px;top:56px;font-family:"Noto Serif",Georgia,serif;font-size:9.5px;color:var(--red)}
.bag-title span{color:#333}
.bag-note{left:641px;top:71px;font-size:7.5px;color:#333}

/* nav */
.nav{left:0;top:93px;width:855px;height:24px;background:linear-gradient(#fbbd3c,#f19d14);border-bottom:1px solid var(--orange-dark)}
.nav ul{position:absolute;left:100px;top:0;list-style:none;display:flex;height:24px}
.nav li{font-size:8.5px;color:#222;padding:0 6px;line-height:24px;border-right:1px solid #d98c12}
.nav li.active{background:var(--nav-active);color:#fff;padding:0 8px}

/* sidebar */
.cat-head{left:100px;top:128px;width:137px;height:22px;background:linear-gradient(#6a6a6a,#4a4a4a);color:#fff;font-size:11px;padding:4px 7px;letter-spacing:.3px}
.cat-list{left:100px;top:154px;width:137px;border:1px solid var(--line);border-top:none;list-style:none}
.cat-list li{height:20px;border-bottom:1px solid #e6e6e6;font-size:8px;line-height:20px;padding-left:6px;color:#333}
.cat-list li:last-child{border-bottom:none}
.cat-list li::before{content:"→";font-size:7px;margin-right:6px}

.deals{left:100px;top:394px;width:137px;height:150px;border:1px solid var(--line);text-align:center}
.deals h3{position:absolute;left:14px;top:-8px;width:107px;font-family:"Noto Serif",Georgia,serif;font-weight:400;font-size:11.5px;line-height:16px;color:#2b7a1b;background:#fff}
.deals-cover{left:37px;top:20px;width:53px;height:72px;background:linear-gradient(135deg,#3a3a48,#111)}
.deals p{position:absolute;left:0;top:95px;width:137px;font-size:8px;line-height:13px}
.deals-price{left:14px;top:128px;font-size:9.5px;font-weight:700;color:var(--red)}
.deals-more{left:80px;top:129px;width:43px;height:11px;border-radius:6px;background:linear-gradient(#6eb7ea,#2a86c9);color:#fff;font-size:6px;line-height:11px}

.social{left:100px;top:558px;width:137px;height:163px;border:1px solid var(--line);font-size:7px}
.social-logo{left:8px;top:7px;width:26px;height:26px;background:#e8d94a}
.social-name{left:46px;top:9px;color:#3b5998}
.social-name span{color:#666}
.social-like{left:41px;top:22px;width:31px;height:14px;border:1px solid #aab;background:#eef;color:#3b5998;font-size:7px;text-align:center;line-height:12px}
.social-signup{left:89px;top:22px;width:41px;height:16px;background:#5fa338;border:1px solid #3f7f22;color:#fff;font-size:8.5px;font-weight:600;text-align:center;line-height:14px}
.social-count{left:6px;top:47px;color:#444}
.social-count span{color:#3b5998}
.fans{left:6px;top:60px;display:grid;grid-template-columns:repeat(3,36px);row-gap:5px}
.fan-photo{width:26px;height:26px;background:linear-gradient(#c9a48f,#7c5c4b)}
.fan-name{font-size:7px;color:#333;margin-top:2px;height:9px}
.social-foot{left:0;bottom:0;width:135px;height:13px;border-top:1px solid #e0e0e0;font-size:6px;color:#666;padding:2px 6px;display:flex;align-items:center;gap:4px}
.social-foot i{width:7px;height:7px;background:#3b5998;display:inline-block}

.pay{left:108px;border:1px solid var(--line);background:#fff}
.pay-a{top:740px;width:121px;height:39px}
.pay-b{top:786px;width:121px;height:30px}
.pay .bar{position:absolute;left:10px;top:3px;width:92px;height:12px;background:#dfe8f4}
.pay-a .bar{border-bottom:2px solid var(--orange)}
.pay .chips{position:absolute;left:6px;display:flex;gap:7px}
.pay-a .chips{top:18px}
.pay-b .chips{top:12px}
.pay .chips i{width:23px;height:15px;border:1px solid #bbb;background:#eceff3;display:block}

/* banner */
.banner{left:251px;top:128px;width:503px;height:248px;border-radius:4px;background:radial-gradient(ellipse at 70% 70%,#3e5a7d 0%,#22364f 55%,#16243a 100%);overflow:hidden}
.devices{left:262px;top:78px;width:212px;height:146px;border-radius:6px;background:linear-gradient(135deg,#8fb8e0,#3f5f80)}
.banner h1{position:absolute;left:27px;top:24px;font-family:"Oswald",Impact,sans-serif;font-weight:400;font-size:28px;line-height:42px;color:#dfe3e8;letter-spacing:.2px;white-space:nowrap}
.banner h1 .gap{display:inline-block;width:58px}
.badge{left:78px;top:59px;width:50px;height:50px;border-radius:50%;background:radial-gradient(#ffcc33,#f39c12);color:#fff;font-family:"Oswald",Impact,sans-serif;font-size:12px;line-height:12px;text-align:center;padding-top:12px;border:2px solid #fff3c0}
.buy{left:34px;top:153px;width:96px;height:26px;border-radius:13px;background:linear-gradient(#4a4f57,#1e2126);border:2px solid #6b7380;color:#fff;font-family:"Oswald",Impact,sans-serif;font-size:14px;text-align:center;line-height:21px}
.dots{left:20px;top:218px;display:flex;gap:4px}
.dots i{width:8px;height:8px;border-radius:50%;background:#111;display:block}
.dots i:first-child{background:#fff}

/* product cards */
.card{width:163px;height:194px;border:1px solid var(--line);background:#fff}
.card-head{position:absolute;left:0;top:0;width:161px;height:28px}
.card-title{position:absolute;left:7px;top:7px;font-size:10.5px;font-weight:600;text-transform:uppercase}
.card-corner{position:absolute;right:2px;top:2px}
.card-desc{position:absolute;left:6px;top:36px;width:102px;font-size:7px;line-height:10px;color:#444}
.card-tag{position:absolute;left:107px;top:27px;width:55px;height:34px;color:#fff;padding:3px 0 0 6px}
.card-tag small{display:block;font-size:7.5px;line-height:9px}
.card-tag b{display:block;font-weight:400;font-size:15px;line-height:18px}
.card-plus{position:absolute;left:153px;top:61px;width:8px;height:8px;background:#333;color:#fff;font-size:7px;line-height:7px;text-align:center}
.card-photo{position:absolute;left:35px;top:72px;width:92px;height:96px;border-radius:3px}
.card-reg{position:absolute;left:4px;bottom:4px;font-size:7px;color:#444}
.c1 .card-head{background:var(--card1-bg)}.c1 .card-title{color:var(--card1-ink)}.c1 .card-tag{background:var(--card1-tag)}
.c2 .card-head{background:var(--card2-bg)}.c2 .card-title{color:var(--card2-ink)}.c2 .card-tag{background:var(--card2-tag)}
.c3 .card-head{background:var(--card3-bg)}.c3 .card-title{color:var(--card3-ink)}.c3 .card-tag{background:var(--card3-tag)}

/* footer */
.footer{left:0;top:1015px;width:855px;height:185px;background:var(--footer)}
.footer h4{position:absolute;top:23px;font-family:"Noto Serif",Georgia,serif;font-weight:400;font-size:12.5px;color:var(--gold)}
.f-input{left:100px;width:118px;height:21px;border-radius:3px;background:#2d3d52;border:1px solid #4a5a70;color:#9aa7b8;font-size:8px;padding:5px 8px}
.f-submit{left:102px;top:121px;width:47px;height:19px;border-radius:3px;background:linear-gradient(#a8a8a8,#6f6f6f);color:#fff;font-size:9px;text-align:center;line-height:18px}
.f-divider{top:22px;width:1px;height:118px;background:var(--footer-line)}
.f-links{list-style:none;font-size:8px;color:#fff;line-height:17.3px}
.f-contact{left:508px;top:54px;font-size:8px;line-height:14px;color:#fff}
.f-line{left:646px;display:flex;align-items:center;gap:6px;font-size:8.5px;color:var(--gold)}
.f-rule{left:0;top:145px;width:855px;height:1px;background:var(--footer-line)}
.copyright{left:100px;top:164px;font-size:8px;color:#fff}
.f-social{left:691px;top:159px;display:flex;gap:4px}
.f-social i{width:19px;height:19px;border-radius:50%;background:#fff;display:block}
</style>
</head>
<body>

<header>
  <div class="abs topbar"></div>
  <nav class="abs toplinks"><span>About US</span><span class="sep">|</span><span>Order Status</span><span class="sep">|</span><span>Wishlist</span><span class="sep">|</span><span>My Account</span><span class="sep">|</span><span>Sign In</span></nav>
  <div class="abs top-phone">
    <svg width="11" height="13" viewBox="0 0 11 13"><path d="M2 0.5 L4 0.5 L5 3.5 L3.5 4.5 Q4.5 7.5 6.5 9 L8 7.8 L10.5 9.5 L9.8 12 Q5 12 2.2 7 Q0.5 3.5 2 0.5Z" fill="#f08c1a"/></svg>
    123 456 7890
  </div>
  <div class="abs live-help">
    <svg width="20" height="13" viewBox="0 0 20 13"><ellipse cx="10" cy="5.5" rx="9.5" ry="5.3" fill="#7ac143"/><path d="M4 9 L2.5 13 L8 10Z" fill="#7ac143"/></svg>
    Live Help
  </div>

  <div class="abs brand"><div class="brand-square"></div><div class="brand-name">sofadeals</div></div>
  <div class="abs promo"><em>FREE Express Shipping</em> with Membership</div>

  <form class="abs search">
    <div class="abs search-cat">All Categories</div>
    <div class="abs search-input">Enter search keyword here...</div>
    <div class="abs search-btn"><svg width="12" height="12" viewBox="0 0 12 12"><circle cx="5" cy="5" r="3.6" fill="none" stroke="#fff" stroke-width="1.6"/><path d="M7.6 7.6 L11 11" stroke="#fff" stroke-width="1.8"/></svg></div>
  </form>

  <div class="abs slogan">Lazy is good!</div>
  <svg class="abs bag" width="28" height="40" viewBox="0 0 28 40"><path d="M9 10 Q9 3 14 3 Q19 3 19 10" fill="none" stroke="#1d6fb0" stroke-width="1.6"/><path d="M3 10 L25 10 L27 39 L1 39Z" fill="#2a8ad6"/><path d="M3 10 L12 10 L9 39 L1 39Z" fill="#57aee8"/></svg>
  <div class="abs bag-title">Shopping Bag <span>(0 items)</span></div>
  <div class="abs bag-note">Spend ₦25, Get FREE SHIPPING</div>

  <nav class="abs nav">
    <ul>
      <li class="active">Mobile Phones</li><li>Laptop &amp; Desktop Computers</li><li>Tablet PCs</li><li>Printers</li><li>Cameras</li><li>Video Games</li><li>Televisions</li><li>DVD Players</li><li>AC</li><li>Fridges</li><li>Inverters</li>
    </ul>
  </nav>
</header>

<aside>
  <div class="abs cat-head">CATEGORIES</div>
  <ul class="abs cat-list">
    <li>Mobile Phones</li><li>Laptop &amp; Desktop Computers</li><li>Tablet PCs</li><li>Printers</li><li>Cameras</li><li>Video Games</li><li>Televisions</li><li>DVD Players</li><li>AC</li><li>Fridges</li><li>Inverters</li>
  </ul>

  <section class="abs deals">
    <h3>Deals of the Week</h3>
    <div class="abs deals-cover" role="img" aria-label="Book cover of the featured deal"></div>
    <p>Lorem ipsum dolor<br>adipiscing elit.</p>
    <div class="abs deals-price">₦249.99</div>
    <div class="abs deals-more">Learn More</div>
  </section>

  <section class="abs social">
    <div class="abs social-logo"></div>
    <div class="abs social-name">Sofadeals <span>-on Friendnet</span></div>
    <div class="abs social-like">Like</div>
    <div class="abs social-signup">Sign Up</div>
    <div class="abs social-count">560 people like <span>Sofadeals</span></div>
    <div class="abs fans">
      <div><div class="fan-photo" role="img" aria-label="Profile photo of Tessa"></div><div class="fan-name">Tessa</div></div>
      <div><div class="fan-photo" role="img" aria-label="Profile photo of Marlo"></div><div class="fan-name">Marlo</div></div>
      <div><div class="fan-photo" role="img" aria-label="Profile photo of Anika"></div><div class="fan-name">Anika</div></div>
      <div><div class="fan-photo" role="img" aria-label="Profile photo of Lina"></div><div class="fan-name">Lina</div></div>
      <div><div class="fan-photo" role="img" aria-label="Profile photo of Brent"></div><div class="fan-name">Brent</div></div>
      <div><div class="fan-photo" role="img" aria-label="Profile photo of Rosalind"></div><div class="fan-name">Rosalind</div></div>
    </div>
    <div class="abs social-foot"><i></i>Friendnet social plugin</div>
  </section>

  <div class="abs pay pay-a" role="img" aria-label="Accepted payment methods"><div class="bar"></div><div class="chips"><i></i><i></i><i></i><i></i></div></div>
  <div class="abs pay pay-b" role="img" aria-label="Accepted checkout methods"><div class="bar"></div><div class="chips"><i></i><i></i><i></i><i></i></div></div>
</aside>

<main>
  <section class="abs banner">
    <div class="abs devices" role="img" aria-label="Laptop, tablet and phone with sky wallpaper"></div>
    <h1>I WAS LAZY TODAY AND<br>GOT <span class="gap"></span> MY LAPTOP</h1>
    <div class="abs badge">20%<br>OFF</div>
    <div class="abs buy">BUY NOW!</div>
    <div class="abs dots"><i></i><i></i><i></i><i></i><i></i></div>
  </section>

  <article class="abs card c1" style="left:251px;top:390px">
    <div class="card-head"><h2 class="card-title">Mobile Phones</h2><svg class="card-corner" width="8" height="8"><path d="M0 0H8V8Z" fill="#7a6a64"/></svg></div>
    <p class="card-desc">Lorem ipsum dolor sit amet, consectetuer adipiscing elit.</p>
    <div class="card-tag"><small>Products</small><b>5,325</b></div><div class="card-plus">+</div>
    <div class="card-photo" role="img" aria-label="Smartphone front and back" style="background:linear-gradient(#4a4a4a,#111)"></div>
    <div class="card-reg">Register For Details</div>
  </article>
  <article class="abs card c2" style="left:421px;top:390px">
    <div class="card-head"><h2 class="card-title">Laptop &amp; Computer</h2><svg class="card-corner" width="8" height="8"><path d="M0 0H8V8Z" fill="#3f8a6a"/></svg></div>
    <p class="card-desc">Lorem ipsum dolor sit amet, consectetuer adipiscing elit.</p>
    <div class="card-tag"><small>Products</small><b>5,325</b></div><div class="card-plus">+</div>
    <div class="card-photo" role="img" aria-label="Black laptop" style="background:linear-gradient(#3a3a3a,#111)"></div>
    <div class="card-reg">Register For Details</div>
  </article>
  <article class="abs card c3" style="left:592px;top:390px">
    <div class="card-head"><h2 class="card-title">Tablets PCs</h2><svg class="card-corner" width="8" height="8"><path d="M0 0H8V8Z" fill="#d4560f"/></svg></div>
    <p class="card-desc">Lorem ipsum dolor sit amet, consectetuer adipiscing elit.</p>
    <div class="card-tag"><small>Products</small><b>5,325</b></div><div class="card-plus">+</div>
    <div class="card-photo" role="img" aria-label="Tablet front and back" style="background:linear-gradient(#555,#1a1a1a)"></div>
    <div class="card-reg">Register For Details</div>
  </article>

  <article class="abs card c1" style="left:251px;top:592px">
    <div class="card-head"><h2 class="card-title">Printers</h2><svg class="card-corner" width="8" height="8"><path d="M0 0H8V8Z" fill="#7a6a64"/></svg></div>
    <p class="card-desc">Lorem ipsum dolor sit amet, consectetuer adipiscing elit.</p>
    <div class="card-tag"><small>Products</small><b>5,325</b></div><div class="card-plus">+</div>
    <div class="card-photo" role="img" aria-label="Inkjet printer" style="background:linear-gradient(#444,#0f0f0f)"></div>
    <div class="card-reg">Register For Details</div>
  </article>
  <article class="abs card c2" style="left:421px;top:592px">
    <div class="card-head"><h2 class="card-title">Cameras</h2><svg class="card-corner" width="8" height="8"><path d="M0 0H8V8Z" fill="#3f8a6a"/></svg></div>
    <p class="card-desc">Lorem ipsum dolor sit amet, consectetuer adipiscing elit.</p>
    <div class="card-tag"><small>Products</small><b>5,325</b></div><div class="card-plus">+</div>
    <div class="card-photo" role="img" aria-label="Silver compact camera" style="background:linear-gradient(#d8d8d8,#8a8a8a)"></div>
    <div class="card-reg">Register For Details</div>
  </article>
  <article class="abs card c3" style="left:592px;top:592px">
    <div class="card-head"><h2 class="card-title">Video Games</h2><svg class="card-corner" width="8" height="8"><path d="M0 0H8V8Z" fill="#d4560f"/></svg></div>
    <p class="card-desc">Lorem ipsum dolor sit amet, consectetuer adipiscing elit.</p>
    <div class="card-tag"><small>Products</small><b>5,325</b></div><div class="card-plus">+</div>
    <div class="card-photo" role="img" aria-label="Handheld game console" style="background:linear-gradient(#3a3a3a,#111)"></div>
    <div class="card-reg">Register For Details</div>
  </article>

  <article class="abs card c1" style="left:251px;top:793px">
    <div class="card-head"><h2 class="card-title">Fridges</h2><svg class="card-corner" width="8" height="8"><path d="M0 0H8V8Z" fill="#7a6a64"/></svg></div>
    <p class="card-desc">Lorem ipsum dolor sit amet, consectetuer adipiscing elit.</p>
    <div class="card-tag"><small>Products</small><b>5,325</b></div><div class="card-plus">+</div>
    <div class="card-photo" role="img" aria-label="Two silver fridges, one open" style="background:linear-gradient(#e6e6e6,#a9a9a9)"></div>
    <div class="card-reg">Register For Details</div>
  </article>
  <article class="abs card c2" style="left:421px;top:793px">
    <div class="card-head"><h2 class="card-title">Inverters</h2><svg class="card-corner" width="8" height="8"><path d="M0 0H8V8Z" fill="#3f8a6a"/></svg></div>
    <p class="card-desc">Lorem ipsum dolor sit amet, consectetuer adipiscing elit.</p>
    <div class="card-tag"><small>Products</small><b>5,325</b></div><div class="card-plus">+</div>
    <div class="card-photo" role="img" aria-label="Black power inverter" style="background:linear-gradient(#3a3a3a,#0d0d0d)"></div>
    <div class="card-reg">Register For Details</div>
  </article>
  <article class="abs card c3" style="left:592px;top:793px">
    <div class="card-head"><h2 class="card-title">AC</h2><svg class="card-corner" width="8" height="8"><path d="M0 0H8V8Z" fill="#d4560f"/></svg></div>
    <p class="card-desc">Lorem ipsum dolor sit amet, consectetuer adipiscing elit.</p>
    <div class="card-tag"><small>Products</small><b>5,325</b></div><div class="card-plus">+</div>
    <div class="card-photo" role="img" aria-label="Window air conditioner" style="background:linear-gradient(#f0f0f0,#c4c4c4)"></div>
    <div class="card-reg">Register For Details</div>
  </article>
</main>

<footer class="abs footer">
  <h4 style="left:100px">Our Newsletter!</h4>
  <div class="abs f-input" style="top:58px">Enter your name...</div>
  <div class="abs f-input" style="top:86px">Enter your email...</div>
  <div class="abs f-submit">Submit</div>

  <div class="abs f-divider" style="left:258px"></div>
  <h4 style="left:285px">Quick Links</h4>
  <ul class="abs f-links" style="left:285px;top:52px"><li>Mobile Phones</li><li>Tablet PCs</li><li>Printers</li><li>Cameras</li><li>Video Games</li></ul>
  <ul class="abs f-links" style="left:397px;top:52px;line-height:16px"><li>Televisions</li><li>DVD Players</li><li>AC</li><li>Fridges</li><li>Inverters</li></ul>

  <div class="abs f-divider" style="left:480px"></div>
  <h4 style="left:507px">Contact Us</h4>
  <p class="abs f-contact">Lorem ipsum dolor sit amet,<br>Consectetuer adipiscing elit,<br>Laoreet dolore magna.</p>
  <div class="abs f-line" style="top:52px"><svg width="10" height="11" viewBox="0 0 11 13"><path d="M2 0.5 L4 0.5 L5 3.5 L3.5 4.5 Q4.5 7.5 6.5 9 L8 7.8 L10.5 9.5 L9.8 12 Q5 12 2.2 7 Q0.5 3.5 2 0.5Z" fill="#fff"/></svg>123 456 7890</div>
  <div class="abs f-line" style="top:71px"><svg width="10" height="8" viewBox="0 0 10 8"><rect x="0.5" y="0.5" width="9" height="7" fill="none" stroke="#fff"/><path d="M0.5 0.5 L5 4.5 L9.5 0.5" fill="none" stroke="#fff"/></svg>info@sofadeals.com</div>

  <div class="abs f-rule"></div>
  <div class="abs copyright">Copyright©2012 Sofadeals. All Rights Reserved.</div>
  <div class="abs f-social"><i></i><i></i><i></i></div>
</footer>

</body>
</html>
```